Brevant Business Card

I have a business that is called "Brevant Electrical Products LTD" My company deals with top of the range laptops and mobile phones that are exclusive. I need a business card that will be eye catching but not over complicated.

Target Market(s)

Adults aged 19 to 50
Upper middle class

Industry/Entity Type

Business

Requirements
Must have
• Company name/logo (file attached)
• It must have my contact information which is:

• Name: Dale Marwick

• Position: Managing Director 

• Business Address: 7 Hapton Row, London, W4 9QD

• Contact Number: 02085193604
• Mobile: 07814260537
• Email: info@brevant-goods.co.uk
Nice to have
• Simple and stylish
• Eye catching

```html
<!DOCTYPE html>
<html lang="en">
<head>
<meta charset="utf-8">
<title>Brevant Electrical Products – Business Card</title>
<link href="https://fonts.googleapis.com/css2?family=Arimo:wght@400&display=swap" rel="stylesheet">
<style>
  :root {
    --page: #ffffff;
    --card: #000000;
    --brand-blue: #1ba3d6;
    --brand-red: #e8202a;
    --detail-grey: #a7a9ac;
  }
  * { margin: 0; padding: 0; box-sizing: border-box; }
  html, body {
    width: 960px;
    height: 1200px;
    overflow: hidden;
    background: var(--page);
    font-family: "Arimo", Arial, sans-serif;
  }
  .sheet { position: relative; width: 960px; height: 1200px; }
  .card {
    position: absolute;
    width: 872px;
    background: var(--card);
  }
  .card--front { left: 46px; top: 15px; height: 570px; }
  .card--back  { left: 42px; top: 617px; height: 568px; }

  .wordmark {
    position: absolute;
    color: var(--brand-blue);
    font-weight: 400;
    line-height: 1;
    white-space: nowrap;
  }
  .tagline {
    position: absolute;
    color: var(--brand-red);
    line-height: 1;
    white-space: nowrap;
  }
  .card--front .wordmark { left: 58px; top: 368px; font-size: 100px; }
  .card--front .tagline  { left: 58px; top: 480px; font-size: 40px; letter-spacing: 5.5px; }

  .card--back .wordmark { left: 584px; top: 433px; font-size: 49px; }
  .card--back .tagline  { left: 584px; top: 488px; font-size: 24px; }

  .contact {
    position: absolute;
    right: 439px;
    top: 52px;
    text-align: right;
    white-space: nowrap;
  }
  .contact__name {
    color: var(--brand-red);
    font-size: 24px;
    line-height: 28px;
    letter-spacing: 0.4px;
    margin-bottom: 19px;
  }
  .contact__details {
    color: var(--detail-grey);
    font-size: 24px;
    line-height: 26.5px;
    letter-spacing: 0.4px;
    font-style: normal;
  }
</style>
</head>
<body>
<main class="sheet">
  <section class="card card--front" aria-label="Card front">
    <div class="wordmark">BREVANT</div>
    <div class="tagline">Electrical Products</div>
  </section>

  <section class="card card--back" aria-label="Card back">
    <div class="contact">
      <p class="contact__name">Dale Marwick</p>
      <address class="contact__details">
        Managing Director<br>
        7 Hapton Row<br>
        London W4 9QD<br>
        P: +44 20 8519 3604<br>
        M: +44 7814 260 537<br>
        E: info@brevant-goods.co.uk
      </address>
    </div>
    <div class="wordmark">BREVANT</div>
    <div class="tagline">Electrical Products</div>
  </section>
</main>
</body>
</html>
```